PowerPoint Design for KELPO Polls

KELPO Polls stands for 'Kindred Estimates Linking Population Outlooks Polls'. It is a collaborative research effort to format and combine multiple sources of public opinion data from around the world into merged datasets. We need a Microsoft PowerPoint design for our conference/workshop presentations and instructional videos used as part of our research efforts and crowdsourced development. The design should match the website design and logo, which are attached to this contest (these are the files from previous successful design contests).

Slides will contain a lot of data visualizations, tables with statistical output (lots of numbers), and figures. Bullet points will be used frequently on slides and larg blocks of text should be avided. Margins should be narrow to maximize space used and the size of fonts must be large enough (24-32+) to be visible at the back of classrooms and conference rooms.

I was away at a conference and am now busy with teaching preparation, so I need a few extra days to give adequate feedback.

Target Market(s)

academia, government, non-profits, postgraduates, researchers

Font styles to use
Sans Serif

Colors

Designer to choose colors to be used in the design.

Requirements
Must have
• designs for common slide layouts
Nice to have
• thematic link with website design and logo

```html
<!DOCTYPE html>
<html lang="en">
<head>
<meta charset="utf-8">
<title>KELPO Polls – Presentation Template</title>
<link rel="stylesheet" href="https://fonts.googleapis.com/css2?family=Open+Sans:wght@400;600;700&display=swap">
<style>
:root{
  --blue-dark:#1663b0;
  --blue:#2a86d4;
  --blue-light:#3fa3e3;
  --navy:#1b4f86;
  --ink:#2b2b2b;
  --text:#555a60;
  --paper:#ffffff;
  --stage-light:#eceef1;
  --stage-dark:#343434;
  --row:#eef0f2;
}
*{box-sizing:border-box;margin:0;padding:0}
html,body{width:708px;height:1200px;overflow:hidden}
body{font-family:"Open Sans",Arial,sans-serif;background:var(--stage-dark);position:relative}
.stage-top{position:absolute;left:0;top:0;width:708px;height:476px;background:var(--stage-light)}
.hero{position:absolute;left:54px;top:69px;width:323px;height:182px;transform:scale(1.8576);transform-origin:0 0;box-shadow:0 1px 3px rgba(0,0,0,.15)}
.slide{position:absolute;width:323px;height:182px;background:var(--paper);overflow:hidden;color:var(--text)}
.s1{left:27px;top:509px}.s2{left:364px;top:509px}
.s3{left:27px;top:711px}.s4{left:364px;top:711px}
.s5{left:27px;top:914px}.s6{left:364px;top:914px}

/* title slide */
.title-slide{background:linear-gradient(120deg,#f4f5f7 0%,#e3e6ea 55%,#eef0f2 100%)}
.title-slide .brand{position:absolute;left:9px;top:60px;font-size:11.5px;font-weight:600;color:var(--blue-dark)}
.title-slide .tagline{position:absolute;left:0;top:78px;width:113px;height:14px;background:var(--blue-dark);color:#fff;font-size:8px;line-height:14px;padding-left:9px}
.title-slide .headline{position:absolute;left:8px;top:94px;font-size:27px;font-weight:400;color:var(--ink);letter-spacing:.5px}
.title-slide .subline{position:absolute;left:9px;top:128px;font-size:9.5px;font-weight:700;color:var(--blue-dark)}
.title-slide .footer-bar{position:absolute;left:0;top:161px;width:120px;height:9px;background:var(--blue-dark);color:#fff;font-size:4.5px;line-height:9px;padding-left:18px;letter-spacing:.8px}
.title-slide .ring{position:absolute;left:178px;top:14px;width:140px;height:140px}
.photo-round{position:absolute;border-radius:50%;border:2px solid #fff}

/* content slides */
.slide-title{position:absolute;left:10px;top:9px;font-size:8.5px;font-weight:700;color:var(--blue-dark);border-bottom:.8px solid var(--blue);padding-bottom:1px;text-transform:uppercase}
.slide-title span{font-weight:400;color:var(--blue)}
.corner-brand{position:absolute;right:9px;top:10px;font-size:4px;font-weight:600;color:var(--blue-dark)}
.slide-footer{position:absolute;left:0;right:0;bottom:9px;text-align:center;font-size:3.6px;letter-spacing:1.2px;color:var(--ink)}
.page-no{position:absolute;right:10px;bottom:9px;font-size:3.6px;color:var(--ink)}
.body{font-size:4.2px;line-height:7.2px;text-align:justify}

.s2 .body{position:absolute;left:10px;top:33px;right:10px}
.framed{position:absolute}
.framed .pic{position:absolute;inset:0}
.framed .edge{position:absolute;border:1.2px solid var(--blue)}
.f1{left:12px;top:79px;width:84px;height:37px}
.f2{left:120px;top:105px;width:86px;height:46px}
.f3{left:225px;top:79px;width:86px;height:38px}

.s3 .side-band{position:absolute;left:0;top:14px;width:40px;height:150px;border-radius:0 75px 75px 0;background:var(--blue-dark);opacity:.9}
.s3 .slide-title{left:106px;top:31px}
.s3 .body{position:absolute;left:106px;right:14px}
.s3 .b1{top:49px}.s3 .b2{top:104px}

.s4 .sub{position:absolute;left:10px;top:48px;font-size:4.4px;font-weight:700;color:var(--blue-dark);width:128px;border-bottom:.6px solid var(--blue-dark);padding-bottom:1px}
.s4 .body{position:absolute;left:10px;top:58px;width:138px;text-align:justify}
.s4 .chart{position:absolute;left:178px;top:50px;width:132px;height:98px}

.s5 .intro{position:absolute;left:10px;top:30px;font-size:4.2px}
.data-table{position:absolute;left:10px;top:40px;width:303px;border-collapse:collapse;font-size:3.4px;color:var(--ink)}
.data-table th{background:var(--navy);color:#fff;font-weight:600;height:13px;text-align:left;padding-left:5px}
.data-table td{height:13.7px;padding-left:5px}
.data-table tr:nth-child(even) td{background:var(--row)}
.data-table td:first-child,.data-table th:first-child{width:26px}

.contact-slide{background:linear-gradient(135deg,var(--blue) 0%,#1f74c4 100%);color:#fff}
.contact-slide .ring{position:absolute;left:30px;top:12px;width:158px;height:158px}
.contact-slide .heading{position:absolute;left:230px;top:63px;width:80px;text-align:center;font-size:9px;font-weight:600}
.contact-slide .icons{position:absolute;left:245px;top:80px;width:50px;height:8px}
.contact-slide .lines{position:absolute;left:230px;top:92px;width:80px;text-align:center;font-size:4.3px;line-height:10px}
.contact-slide .brand{position:absolute;left:218px;top:151px;width:100px;text-align:right;font-size:9px;font-weight:600}

.wordmark{position:absolute;left:0;right:0;top:1132px;text-align:center;font-size:34px;font-weight:600;color:#fff}
</style>
</head>
<body>

<div class="stage-top"></div>

<!-- Title slide, presented large -->
<section class="slide title-slide hero">
  <div class="photo-round" role="img" aria-label="Photo of hands working on a laptop" style="left:213px;top:49px;width:70px;height:70px;background:radial-gradient(circle at 40% 40%,#cfcac4,#6b625b)"></div>
  <svg class="ring" viewBox="0 0 140 140"><circle cx="70" cy="70" r="52" fill="none" stroke="var(--blue)" stroke-width="3"/></svg>
  <div class="brand">KELPO Polls</div>
  <div class="tagline">Aliquam ac magna nec</div>
  <div class="headline">LOREM</div>
  <div class="subline">EUISMOD CONGUE</div>
  <div class="footer-bar">www.kelpopolls.org</div>
</section>

<!-- Title slide -->
<section class="slide title-slide s1">
  <div class="photo-round" role="img" aria-label="Photo of hands working on a laptop" style="left:213px;top:49px;width:70px;height:70px;background:radial-gradient(circle at 40% 40%,#cfcac4,#6b625b)"></div>
  <svg class="ring" viewBox="0 0 140 140"><circle cx="70" cy="70" r="52" fill="none" stroke="var(--blue)" stroke-width="3"/></svg>
  <div class="brand">KELPO Polls</div>
  <div class="tagline">Aliquam ac magna nec</div>
  <div class="headline">LOREM</div>
  <div class="subline">EUISMOD CONGUE</div>
  <div class="footer-bar">www.kelpopolls.org</div>
</section>

<!-- About slide -->
<section class="slide s2">
  <h2 class="slide-title">About KELPO <span>Survey</span></h2>
  <div class="corner-brand">KELPO Polls</div>
  <p class="body">KELPO Polls make it easier to work with multiple sources of public opinion data. It does so by formatting variables for consistency and merging datasets together. The current merged dataset includes millions of respondents, covers most countries in the world, and extends back decades. This increased variation over time and space enables answering new research questions with greater reliability.</p>
  <div class="framed f1"><span class="edge" style="left:-3px;top:-3px;width:40px;height:22px;border-right:0;border-bottom:0"></span><div class="pic" role="img" aria-label="Photo of a person typing on a laptop" style="background:linear-gradient(135deg,#b98c6c,#e9e2da)"></div><span class="edge" style="right:-3px;bottom:-3px;width:40px;height:22px;border-left:0;border-top:0"></span></div>
  <div class="framed f2"><span class="edge" style="left:-3px;top:-3px;width:40px;height:22px;border-right:0;border-bottom:0"></span><div class="pic" role="img" aria-label="Photo of hands holding a phone over a laptop" style="background:linear-gradient(135deg,#4a3b3a,#c7b7b0)"></div><span class="edge" style="right:-3px;bottom:-3px;width:40px;height:22px;border-left:0;border-top:0"></span></div>
  <div class="framed f3"><span class="edge" style="left:-3px;top:-3px;width:40px;height:22px;border-right:0;border-bottom:0"></span><div class="pic" role="img" aria-label="Photo of a woman on the phone at a desk" style="background:linear-gradient(135deg,#5f7a4a,#d8d2c8)"></div><span class="edge" style="right:-3px;bottom:-3px;width:40px;height:22px;border-left:0;border-top:0"></span></div>
  <div class="slide-footer">www.kelpopolls.org</div>
  <div class="page-no">01</div>
</section>

<!-- Text slide -->
<section class="slide s3">
  <div class="side-band"></div>
  <h2 class="slide-title">Etiam dictum <span>urna sagittis</span></h2>
  <div class="corner-brand">KELPO Polls</div>
  <p class="body b1">Variables are available at three levels of analysis within each corresponding dataset: respondent, country-survey, and county-year. At the respondent level, common variables are binary and result from dichotomizing different answer scales. Neutral and midpoint answers are consistently grouped with negative answers, meaning that respondent level variables focus on measuring the presence of what it measures rather than its absence.</p>
  <p class="body b2">Variables are available at three levels of analysis within each corresponding dataset: respondent, country-survey, and county-year. At the respondent level, common variables are binary and result from dichotomizing different answer scales. Neutral and midpoint answers are consistently grouped with negative answers, meaning that respondent level variables focus on measuring the presence of what it measures rather than its absence.</p>
  <div class="slide-footer">www.kelpopolls.org</div>
  <div class="page-no">02</div>
</section>

<!-- Chart slide -->
<section class="slide s4">
  <h2 class="slide-title">KELPO Survey <span>Datasets</span></h2>
  <div class="corner-brand">KELPO Polls</div>
  <div class="sub">ETIAM DICTUM URNA SAGITTIS</div>
  <p class="body">Variables are available at three levels of analysis within each corresponding dataset - Respondent, country-survey, and county-year. At the respondent level, common variables are binary and result from dichotomizing different answer scales. Neutral and midpoint answers are consistently grouped with negative answers, meaning that respondent level variables focus on measuring the presence of what it measures rather than its absence.</p>
  <svg class="chart" viewBox="0 0 132 98">
    <g stroke="#dfe4ea" stroke-width=".5"><line x1="6" y1="24" x2="130" y2="24"/><line x1="6" y1="44" x2="130" y2="44"/><line x1="6" y1="64" x2="130" y2="64"/></g>
    <polygon points="10,82 28,78 46,70 64,78 84,56 104,44 124,36 132,30 132,90 10,90" fill="#cfe3f4" opacity=".8"/>
    <polyline points="10,82 28,78 46,70 64,78 84,56 104,44 124,36 132,30" fill="none" stroke="var(--blue)" stroke-width=".8"/>
    <g fill="var(--blue-dark)"><circle cx="28" cy="78" r="1"/><circle cx="46" cy="70" r="1"/><circle cx="64" cy="78" r="1"/><circle cx="84" cy="56" r="1"/><circle cx="104" cy="44" r="1"/><circle cx="124" cy="36" r="1"/><circle cx="132" cy="30" r="1"/></g>
    <g stroke="var(--blue-dark)" stroke-width=".8" fill="none"><line x1="6" y1="2" x2="6" y2="91"/><line x1="5" y1="90" x2="132" y2="90"/><path d="M4 5 L6 1 L8 5"/></g>
  </svg>
  <div class="slide-footer">www.kelpopolls.org</div>
  <div class="page-no">03</div>
</section>

<!-- Table slide -->
<section class="slide s5">
  <h2 class="slide-title">Quisque risus <span>magna</span></h2>
  <div class="corner-brand">KELPO Polls</div>
  <p class="intro">Lorem ipsum dolor sit amet, consectetur adipiscing elit. Duis ut tortor vitae lorem venenatis rutrum.</p>
  <table class="data-table">
    <tr><th>NO</th><th>CUSTOMER NAME</th><th>ITEMS</th><th>SUBJECT CODE</th><th>SUBJECT CODE</th></tr>
    <tr><td>1</td><td>Dana Whitlow</td><td>Mauris laoreet commodo</td><td>Mauris laoreet commodo</td><td>Mauris laoreet commodo</td></tr>
    <tr><td>2</td><td>Dana Whitlow</td><td>Mauris laoreet commodo</td><td>Mauris laoreet commodo</td><td>Mauris laoreet commodo</td></tr>
    <tr><td>3</td><td>Dana Whitlow</td><td>Mauris laoreet commodo</td><td>Mauris laoreet commodo</td><td>Mauris laoreet commodo</td></tr>
    <tr><td>4</td><td>Dana Whitlow</td><td>Mauris laoreet commodo</td><td>Mauris laoreet commodo</td><td>Mauris laoreet commodo</td></tr>
    <tr><td>5</td><td>Dana Whitlow</td><td>Mauris laoreet commodo</td><td>Mauris laoreet commodo</td><td>Mauris laoreet commodo</td></tr>
    <tr><td>6</td><td>Dana Whitlow</td><td>Mauris laoreet commodo</td><td>Mauris laoreet commodo</td><td>Mauris laoreet commodo</td></tr>
    <tr><td>7</td><td>Dana Whitlow</td><td>Mauris laoreet commodo</td><td>Mauris laoreet commodo</td><td>Mauris laoreet commodo</td></tr>
  </table>
  <div class="slide-footer">www.kelpopolls.org</div>
  <div class="page-no">04</div>
</section>

<!-- Contact slide -->
<section class="slide contact-slide s6">
  <svg class="ring" viewBox="0 0 158 158"><circle cx="79" cy="79" r="60" fill="none" stroke="rgba(255,255,255,.85)" stroke-width="3"/></svg>
  <div class="photo-round" role="img" aria-label="Photo of hands holding a tablet with gear graphics" style="left:80px;top:61px;width:58px;height:58px;background:radial-gradient(circle at 50% 45%,#9aa3ab,#3c4147)"></div>
  <div class="heading">CONTACT US</div>
  <svg class="icons" viewBox="0 0 50 8" fill="none" stroke="#fff" stroke-width=".7">
    <path d="M9 1.5 l1.5 0 l.6 1.6 l-.9 .7 a4 4 0 0 0 2 2 l.7-.9 l1.6 .6 l0 1.5 a5.5 5.5 0 0 1 -5.5 -5.5z" fill="#fff" stroke="none"/>
    <rect x="21" y="2" width="7" height="5"/><path d="M21 2 l3.5 3 l3.5 -3"/>
    <circle cx="38" cy="4.5" r="3"/><ellipse cx="38" cy="4.5" rx="1.2" ry="3"/><line x1="35" y1="4.5" x2="41" y2="4.5"/>
  </svg>
  <div class="lines">555.014.2290<br>info@kelpopolls.org<br>www.kelpopolls.org</div>
  <div class="brand">KELPO Polls</div>
</section>

<div class="wordmark">KELPO Polls</div>

</body>
</html>
```